Infectious Diseases Research Laboratory Needs Business Card

We need a business card for an academic research laboratory based in Kansas City called MORVEK. The full lab name is Microbial Dose-Response/Exposure Bridging Studies Laboratory, but this does not need to be incorporated. We study novel ways to optimize the treatment of multidrug-resistant bacterial infections ("superbugs") throughout the entire biomedical research spectrum (from benchtop to bedside). The name MORVEK is not only an acronym for our lab name, but also represents our desire to make discoveries and explore the unknown (the stars, if you well). It also serves as an ode to the state of Kansas motto where we are based, ad astra per aspera ("to the stars, through difficulty").

Target Market(s)

Pharmaceutical companies, researchers

Industry/Entity Type

Pharmaceutical

Contact Information for Business Card

The business card should incorporate and complement our new logo (see uploaded files). Double-sided designs are preferred. Looking for something modern, but professional.

Font styles to use
Sans Serif

Requirements
Must have
• Double-sided. One side would ideally be a solid color incorporating logo and the other should also have the logo (smaller), but incorporate staff information.
• Color codes:
• Red: #F04C51
• Blue: #3477B5
• Gray: #808285

```html
<!DOCTYPE html>
<html lang="en">
<head>
<meta charset="utf-8">
<title>MORVEK Business Card</title>
<link href="https://fonts.googleapis.com/css2?family=Arimo:wght@400;700&display=swap" rel="stylesheet">
<style>
  :root {
    --red: #F04C51;
    --blue: #3477B5;
    --blue-light: #45A3DA;
    --gray: #808285;
    --white: #ffffff;
    --stage: #ECEDEF;
  }
  * { box-sizing: border-box; margin: 0; padding: 0; }
  html, body { width: 1200px; height: 903px; overflow: hidden; }
  body {
    background: var(--stage);
    font-family: "Arimo", Arial, sans-serif;
    position: relative;
  }
  .card {
    position: absolute;
    width: 500px;
    height: 286px;
    border-radius: 2px;
    overflow: hidden;
    box-shadow: 0 10px 28px rgba(0,0,0,0.18);
  }
  /* Front */
  .card-front {
    left: 80px; top: 150px;
    background: radial-gradient(circle at 35% 70%, var(--blue-light) 0%, var(--blue) 60%, #2E6CAD 100%);
    color: var(--white);
  }
  .wordmark {
    position: absolute;
    display: flex;
    align-items: center;
    gap: 14px;
  }
  .card-front .wordmark { left: 108px; top: 100px; }
  .wordmark-dot {
    border-radius: 50%;
    flex: none;
  }
  .card-front .wordmark-dot { width: 46px; height: 46px; background: var(--white); }
  .wordmark-text { display: flex; flex-direction: column; }
  .wordmark-name {
    font-weight: 400;
    letter-spacing: 4px;
    line-height: 1;
  }
  .card-front .wordmark-name { font-size: 44px; color: var(--white); }
  .wordmark-sub {
    font-size: 5.5px;
    letter-spacing: 0.6px;
    text-transform: uppercase;
    margin-top: 4px;
    padding-top: 3px;
    border-top: 1px solid currentColor;
    white-space: nowrap;
  }
  .front-url {
    position: absolute;
    right: 40px; bottom: 26px;
    font-size: 17px;
    letter-spacing: 0.3px;
  }
  /* Back */
  .card-back {
    left: 620px; top: 450px;
    background: var(--white);
  }
  .card-back .wordmark { right: 26px; top: 30px; gap: 10px; }
  .card-back .wordmark-dot { width: 34px; height: 34px; background: var(--red); }
  .card-back .wordmark-name { font-size: 34px; color: var(--red); letter-spacing: 3px; }
  .card-back .wordmark-sub { color: var(--gray); font-size: 4.6px; }
  .band {
    position: absolute;
    left: 0; right: 0;
    top: 112px; height: 106px;
    background: linear-gradient(90deg, var(--red), #EE3F45);
  }
  .staff {
    position: absolute;
    left: 30px; top: 124px;
    color: var(--white);
  }
  .staff-name { font-size: 19px; font-weight: 700; letter-spacing: 0.3px; }
  .staff-title { font-size: 12px; color: var(--blue); margin-top: 1px; }
  .contact-list { list-style: none; margin-top: 9px; }
  .contact-item {
    display: flex; align-items: center; gap: 8px;
    font-size: 12.5px; line-height: 16px;
  }
  .contact-icon { width: 10px; height: 10px; flex: none; }
  .address {
    position: absolute;
    right: 26px; top: 232px;
    text-align: right;
    font-size: 11.5px;
    line-height: 15px;
    color: #4a4b4d;
  }
</style>
</head>
<body>
  <section class="card card-front" aria-label="Card front">
    <div class="wordmark">
      <span class="wordmark-dot"></span>
      <div class="wordmark-text">
        <span class="wordmark-name">MORVEK</span>
        <span class="wordmark-sub">Microbial Dose-Response/Exposure Bridging Studies Laboratory</span>
      </div>
    </div>
    <p class="front-url">www.morvek.com</p>
  </section>

  <section class="card card-back" aria-label="Card back">
    <div class="wordmark">
      <span class="wordmark-dot"></span>
      <div class="wordmark-text">
        <span class="wordmark-name">MORVEK</span>
        <span class="wordmark-sub">Microbial Dose-Response/Exposure Bridging Studies Laboratory</span>
      </div>
    </div>
    <div class="band"></div>
    <div class="staff">
      <p class="staff-name">Dara Whitlock</p>
      <p class="staff-title">Vice President</p>
      <ul class="contact-list">
        <li class="contact-item">
          <svg class="contact-icon" viewBox="0 0 10 10"><path d="M2 1 L4 1 L4.6 3 L3.5 4 Q4.5 6 6 6.5 L7 5.4 L9 6 L9 8 Q9 9 8 9 Q1 8.5 1 2 Q1 1 2 1Z" fill="var(--blue)"/></svg>
          001 555 0148
        </li>
        <li class="contact-item">
          <svg class="contact-icon" viewBox="0 0 10 10"><rect x="0.5" y="2" width="9" height="6.5" fill="var(--blue)"/><path d="M0.5 2 L5 5.5 L9.5 2" stroke="var(--white)" stroke-width="0.9" fill="none"/></svg>
          info@morvek.com
        </li>
        <li class="contact-item">
          <svg class="contact-icon" viewBox="0 0 10 10"><circle cx="5" cy="5" r="4.2" fill="none" stroke="var(--blue)" stroke-width="1.1"/><ellipse cx="5" cy="5" rx="1.8" ry="4.2" fill="none" stroke="var(--blue)" stroke-width="0.9"/><line x1="0.8" y1="5" x2="9.2" y2="5" stroke="var(--blue)" stroke-width="0.9"/></svg>
          www.morvek.com
        </li>
      </ul>
    </div>
    <p class="address">4120 Linden Avenue, Suite 12<br>Kansas City, KS 66160</p>
  </section>
</body>
</html>
```